Atelier Marrow Architecture business card

We need to update our business card. We do high end custom residential, hospitality, and wellness architecture. We focus on creating unique spaces and design around the five senses, believing that architecture's true impact is not on our surroundings, but within us. We would like to see designs are instill a sense of calm awe. They should be crisp, fresh, clean, authentic, & contemporary without being sterile, overworked, or harsh. White space is important. Alternative materials are an option if natural. We have created our own logo and would like designs to incorporate it. However, we are willing to see alternatives if the logo becomes a stumbling block and you have an alternate you suggest. Card must have the following information:
Atelier Marrow Architecture, Inc.
728 Holloway Ct. NE Atlanta, GA 30318
Marcus T. Whitcombe, AIA, NCARB, LEED AP BD+C
ateliermarrow.example

Target Market(s)

Higher net worth individuals with an appreciation for design, nature, sustainability,

Industry/Entity Type

Architect

Contact Information for Business Card

See above. The title of Owner or Architect is helpful but not necessary. Minimalism should trump additional information.

Font styles to use
Serif
Sans Serif

Requirements
Must have
• It should look professional. It must use logo
Should not have
• caligraphy, animals, anything that is cute,

```html
<!DOCTYPE html>
<html lang="en">
<head>
<meta charset="utf-8">
<title>Atelier Marrow Architecture — Business Card</title>
<link href="https://fonts.googleapis.com/css2?family=Lato:wght@300;400;700;900&display=swap" rel="stylesheet">
<style>
  :root {
    --ink: #231f20;
    --paper: #ffffff;
    --backdrop: #e4e4e2;
    --shadow: rgba(0, 0, 0, 0.14);
  }
  * { margin: 0; padding: 0; box-sizing: border-box; }
  html, body {
    width: 1200px; height: 1200px; overflow: hidden;
    background: var(--backdrop);
    font-family: "Lato", Arial, sans-serif;
    color: var(--ink);
  }
  .card {
    position: absolute; left: 180px;
    width: 840px; height: 480px;
    background: var(--paper);
    box-shadow: 0 6px 24px var(--shadow);
    overflow: hidden;
  }
  .card--front { top: 90px; }
  .card--back { top: 630px; }

  /* Front */
  .brand-band {
    position: absolute; left: 0; top: 190px;
    width: 240px; height: 112px;
    background: var(--ink);
  }
  .brand-dot {
    position: absolute; left: 130px; top: 26px;
    width: 60px; height: 60px; border-radius: 50%;
    background: var(--paper);
  }
  .brand-name {
    position: absolute; left: 282px; top: 212px;
    font-weight: 900; font-size: 38px; letter-spacing: 1px;
    text-transform: uppercase; line-height: 1;
  }
  .brand-tagline {
    position: absolute; left: 284px; top: 260px;
    font-weight: 900; font-size: 11px; letter-spacing: 17.5px;
    text-transform: uppercase;
  }

  /* Back */
  .bracket { position: absolute; }
  .bracket--open { left: 70px; top: 120px; }
  .bracket--close { left: 370px; top: 250px; }
  .person {
    position: absolute; left: 112px; top: 150px;
  }
  .person-name {
    font-size: 30px; font-weight: 300; text-transform: uppercase;
    letter-spacing: 0.5px; line-height: 1.1;
  }
  .person-name strong { font-weight: 900; }
  .person-credentials {
    font-size: 16px; font-weight: 400; margin-top: 10px; letter-spacing: 0.3px;
  }
  .person-company {
    font-size: 14px; font-weight: 400; margin-top: 6px; letter-spacing: 0.3px;
  }
  .contact-band {
    position: absolute; left: 420px; top: 300px;
    width: 420px; height: 112px;
    background: var(--ink); color: var(--paper);
    padding: 20px 0 0 26px;
    font-size: 15px; font-weight: 400; line-height: 1.55;
  }
  .contact-row { display: flex; white-space: nowrap; }
  .contact-label { width: 70px; }
</style>
</head>
<body>
  <section class="card card--front" aria-label="Card front">
    <div class="brand-band"><div class="brand-dot"></div></div>
    <div class="brand-name">Atelier Marrow</div>
    <div class="brand-tagline">Architecture</div>
  </section>

  <section class="card card--back" aria-label="Card back">
    <svg class="bracket bracket--open" width="50" height="110" viewBox="0 0 50 110" aria-hidden="true">
      <polyline points="46,4 6,4 6,106 24,106" fill="none" stroke="var(--ink)" stroke-width="7"/>
    </svg>
    <div class="person">
      <div class="person-name"><strong>Marcus T.</strong> Whitcombe</div>
      <div class="person-credentials">AIA, NCARB, LEED AP BD+C</div>
      <div class="person-company">Atelier Marrow Architecture, Inc.</div>
    </div>
    <svg class="bracket bracket--close" width="40" height="110" viewBox="0 0 40 110" aria-hidden="true">
      <polyline points="14,4 34,4 34,106 4,106" fill="none" stroke="var(--ink)" stroke-width="7"/>
    </svg>
    <div class="contact-band">
      <div class="contact-row"><span class="contact-label">office</span><span>: 728 Holloway Ct. NE Atlanta, GA 30318</span></div>
      <div class="contact-row"><span class="contact-label">email</span><span>: marcus@ateliermarrow.example</span></div>
      <div class="contact-row"><span class="contact-label">website</span><span>: ateliermarrow.example</span></div>
    </div>
  </section>
</body>
</html>
```